Business Card & Letterhead Design

We a financial advice company based in Australia. We provide advice to wealthy farmers.

We are changing our business name FROM Brightmere Financial TO Calderstone Wealth and we need a new letterhead and double sided business card design

Attached is designs from our previous branding (Brightmere Financial) as it includes all the details we require on the new Calderstone Wealth business cards and letterhead.

```html
<!DOCTYPE html>
<html lang="en">
<head>
<meta charset="utf-8">
<title>Calderstone Wealth — Business Card</title>
<link rel="stylesheet" href="https://fonts.googleapis.com/css2?family=Smokum&display=swap">
<style>
  :root {
    --ink: #000000;
    --paper: #ffffff;
  }
  html, body {
    margin: 0;
    padding: 0;
    width: 1200px;
    height: 686px;
    overflow: hidden;
    background: var(--ink);
  }
  .card {
    position: relative;
    width: 1200px;
    height: 686px;
    background: var(--ink);
    color: var(--paper);
    font-family: "Smokum", serif;
  }
  .card-frame {
    position: absolute;
    left: 23px;
    top: 25px;
    right: 23px;
    bottom: 25px;
    border: 8px solid var(--paper);
  }
  .brand {
    position: absolute;
    left: 0;
    right: 0;
    top: 68px;
    text-align: center;
  }
  .brand-circle {
    display: block;
    margin: 0 auto;
  }
  .brand-name {
    margin: 14px 0 0;
    font-size: 34px;
    font-weight: 400;
    letter-spacing: 1px;
    line-height: 1;
  }
  .services {
    position: absolute;
    left: 0;
    right: 0;
    top: 264px;
    margin: 0;
    padding: 0;
    list-style: none;
    text-align: center;
    font-size: 42px;
    line-height: 50.7px;
    letter-spacing: 0.5px;
  }
  .licensee {
    position: absolute;
    left: 0;
    right: 0;
    top: 520px;
    margin: 0;
    text-align: center;
    font-size: 30px;
    line-height: 40px;
    letter-spacing: 0.5px;
  }
</style>
</head>
<body>
  <main class="card">
    <div class="card-frame"></div>

    <header class="brand">
      <svg class="brand-circle" width="84" height="84" viewBox="0 0 84 84" aria-hidden="true">
        <circle cx="42" cy="42" r="38" fill="none" stroke="var(--paper)" stroke-width="6"/>
      </svg>
      <h1 class="brand-name">Calderstone Wealth</h1>
    </header>

    <ul class="services">
      <li>Life &amp; TPD Insurance</li>
      <li>Income Protection</li>
      <li>Financial Planning</li>
      <li>Retirement Planning</li>
    </ul>

    <p class="licensee">
      Harbourline Financial Planning Limited<br>
      Australian Financial Services License Number 418902
    </p>
  </main>
</body>
</html>
```